Website for IT consulting Company

I need a website upgrade, the existing site content is ok, I would also like to add a testimonial page, the site should be something that is easy for us to update content. You use the content from www.velmarketa.com as an example. I will also post update logo and artwork. I also need a contact form with some type of validation or captcha.

Please omit Address maps

Target Market(s)

small business, service oriented companies. We provide IT Consulting, support and mangement

Industry/Entity Type

Information Technology

Coding

Coded - Design and coding required

Number of Pages Required

1 page

Font styles to use
Serif
Sans Serif

Requirements
Must have
• Contain logo attached, and content from existing web site www.velmarketa.com.
• Also need to update content easily, and be movable to different platforms.
• There is a catch phrase
• "Let us worry about your technology…” “ so you don’t have to!”
• Should be included.
Nice to have
• Testimonial page, Project page where we can post new and past projects and pictures
Should not have
• none

```html
<!DOCTYPE html>
<html lang="en">
<head>
<meta charset="utf-8">
<title>Velmarketa – IT Consulting, Support and Management</title>
<link rel="stylesheet" href="https://fonts.googleapis.com/css2?family=Open+Sans:ital,wght@0,400;0,600;0,700;1,400&family=Arimo:ital,wght@0,400;0,700;1,400;1,700&display=swap">
<style>
:root{
  --orange:#f47b20;
  --orange-dark:#e06a12;
  --ink:#333333;
  --muted:#666666;
  --topbar:#1b1b1b;
  --navbar:#222222;
  --light:#f1f1f1;
  --white:#ffffff;
  --line:#d9d9d9;
  --footer:#ececec;
  --bottom:#1f1f1f;
}
*{box-sizing:border-box;margin:0;padding:0}
html,body{width:1200px;height:3502px;overflow:hidden}
body{position:relative;font-family:"Arimo",Arial,sans-serif;color:var(--ink);background:var(--white);font-size:14px;line-height:1.5}
.abs{position:absolute}

/* top bar */
.topbar{left:0;top:0;width:1200px;height:110px;background:var(--topbar)}
.tagline{left:65px;top:24px;font-family:"Open Sans",sans-serif;font-weight:700;font-size:30px;color:var(--orange);letter-spacing:.2px}
.tagline-sub{left:65px;top:69px;font-family:"Open Sans",sans-serif;font-weight:700;font-size:13px;color:var(--white)}
.social-top{left:930px;top:34px;display:flex;gap:6px}
.social-top span,.social-foot span{display:block;width:19px;height:19px;background:#555;border-radius:2px}
.search{left:1118px;top:34px}

/* nav */
.navbar{left:0;top:110px;width:1200px;height:107px;background:var(--navbar)}
.brand{left:65px;top:138px;display:flex;align-items:center;gap:12px}
.brand i{display:block;width:40px;height:40px;background:var(--orange)}
.brand b{font-family:"Open Sans",sans-serif;font-weight:700;font-size:34px;color:var(--white);letter-spacing:1px}
.nav{left:553px;top:147px;display:flex;gap:0;font-family:"Open Sans",sans-serif;font-weight:600;font-size:14px;color:var(--white)}
.nav a{color:var(--white);text-decoration:none;padding:6px 14px;margin-right:33px;line-height:21px}
.nav a.active{background:var(--orange);border-radius:2px}

/* hero */
.hero{left:0;top:217px;width:1200px;height:472px;background:linear-gradient(120deg,#c9b59c 0%,#e8e4dc 35%,#b9d0e4 60%,#6d8fb0 100%)}
.hero-shade{left:0;top:217px;width:1200px;height:472px;background:linear-gradient(90deg,rgba(20,20,20,.45) 0%,rgba(20,20,20,.15) 45%,rgba(0,0,0,0) 70%)}
.hero-title{left:65px;top:355px;width:560px;font-family:"Open Sans",sans-serif;font-weight:600;font-size:35px;line-height:40px;color:var(--white)}
.hero-sub{left:65px;top:447px;font-family:"Open Sans",sans-serif;font-weight:700;font-size:14px;color:var(--white)}
.btn{background:var(--orange);color:var(--white);font-family:"Open Sans",sans-serif;font-weight:700;text-align:center;border-radius:2px}
.hero-btn{left:65px;top:500px;width:103px;height:35px;line-height:35px;font-size:13px}
.arrow{top:427px;width:38px;height:40px;background:var(--orange);border-radius:2px}
.dot{top:630px;width:24px;height:24px;border-radius:50%}

/* IT support */
.support{left:0;top:689px;width:1200px;height:555px;background:var(--light)}
.sec-title{width:1200px;left:0;text-align:center;font-family:"Open Sans",sans-serif;font-weight:600;font-size:36px}
.sec-lead{left:280px;width:640px;text-align:center;font-size:14px;line-height:20px}
.svc-icon{width:98px;height:98px;border-radius:50%;background:var(--white);box-shadow:0 0 0 6px #e6e6e6;display:flex;align-items:center;justify-content:center}
.svc-title{font-family:"Open Sans",sans-serif;font-weight:600;font-size:13px;text-transform:uppercase;letter-spacing:.3px}
.svc-text{font-size:14px;line-height:21px;color:var(--muted);width:220px}

/* flexible */
.flex-bg{left:0;top:1244px;width:1200px;height:1060px;background:radial-gradient(ellipse at 60% 40%,#3a3a3a 0%,#262626 50%,#181818 100%)}
.flex-title{top:1306px;color:var(--white);font-weight:700;font-family:"Open Sans",sans-serif;font-size:35px}
.flex-lead{left:65px;top:1364px;width:1070px;text-align:center;color:var(--white);font-size:14px;line-height:22px;font-weight:700}
.flex-lead em{font-style:italic}
.card{width:337px;height:330px;background:var(--white)}
.card svg{position:absolute;left:22px;top:32px}
.card h3{position:absolute;left:108px;top:42px;width:210px;font-family:"Open Sans",sans-serif;font-weight:400;font-size:18px;line-height:22px;color:#555}
.card p{position:absolute;left:108px;top:108px;width:205px;font-size:13px;line-height:20px;color:var(--ink)}
.card.short p{top:84px}

/* contact */
.contact-sec{left:0;top:2304px;width:1200px;height:451px;background:#f3f3f3}
.col-title{font-family:"Open Sans",sans-serif;font-weight:600;font-size:20px}
.rule{height:1px;background:var(--line)}
.field{left:65px;width:495px;height:38px;background:var(--white);border:1px solid #d6d6d6;border-radius:2px;padding:9px 12px;font-size:12px;color:#888}
.send{left:65px;top:2645px;width:187px;height:34px;line-height:34px;font-size:18px;font-family:"Arimo",sans-serif}
.why-text{left:614px;top:2449px;width:521px;font-size:14px;line-height:24px}

/* tabs */
.tabs-box{left:65px;top:2818px;width:705px;height:240px;background:var(--white);border:1px solid #e2e2e2}
.tab-list{left:65px;top:2818px;width:175px;height:240px;background:#f4f4f4;border-right:1px solid #e2e2e2}
.tab{left:65px;width:175px;height:47px;line-height:47px;padding-left:14px;font-size:12px;color:#555;border-bottom:1px solid #e2e2e2}
.tab.active{background:var(--navbar);color:var(--white);font-weight:700;width:188px}
.tab.active::after{content:"";position:absolute;right:-14px;top:0;border-left:14px solid var(--navbar);border-top:23.5px solid transparent;border-bottom:23.5px solid transparent}
.tab-photo{left:278px;top:2839px;width:194px;height:180px;background:linear-gradient(135deg,#6e8fa8 0%,#c9a387 45%,#e3cdb6 70%,#8f8a86 100%)}
.tab-head{left:490px;top:2836px;font-weight:700;font-size:15px}
.tab-text{left:490px;top:2866px;width:258px;font-size:13px;line-height:20px}
.testi-title{left:798px;top:2818px;font-size:15px;font-weight:700}
.quote{left:810px;width:330px;border-left:1px solid #cfcfcf;padding-left:22px;font-size:13px;line-height:20px}
.quote cite{display:block;margin-top:8px;font-style:normal;font-size:12px}
.quote cite b{font-weight:700}

/* footer */
.footer{left:0;top:3145px;width:1200px;height:275px;background:var(--footer)}
.foot-title{top:3208px;font-family:"Open Sans",sans-serif;font-size:21px;font-weight:400;text-transform:uppercase}
.foot-text{font-size:12px;line-height:28px}
.news-field{left:614px;top:3262px;width:157px;height:38px;background:var(--white);border:1px solid #cfcfcf;padding:9px 8px;font-size:12px;color:#888}
.join{left:614px;top:3314px;width:82px;height:34px;line-height:34px;font-size:18px}
.social-foot{left:887px;top:3262px;display:flex;gap:6px}
.social-foot span{background:#333}
.orange-line{left:0;top:3418px;width:1200px;height:6px;background:var(--orange)}
.bottombar{left:0;top:3424px;width:1200px;height:78px;background:var(--bottom)}
.copy{left:65px;top:3452px;font-size:12px;color:var(--white)}
.foot-nav{left:862px;top:3452px;display:flex;gap:24px;font-size:12px;color:var(--white)}
</style>
</head>
<body>

<!-- top bar -->
<div class="abs topbar"></div>
<div class="abs tagline">LET US WORRY ABOUT YOUR TECHNOLOGY...</div>
<div class="abs tagline-sub">SO YOU DON'T HAVE TO!</div>
<div class="abs social-top" aria-label="Social links"><span></span><span></span><span></span><span></span><span></span><span></span></div>
<svg class="abs search" width="16" height="16" viewBox="0 0 16 16" aria-label="Search"><circle cx="6.5" cy="6.5" r="4.5" fill="none" stroke="#fff" stroke-width="2"/><line x1="10" y1="10" x2="14" y2="14" stroke="#fff" stroke-width="2"/></svg>

<!-- navigation -->
<div class="abs navbar"></div>
<div class="abs brand"><i></i><b>VELMARKETA</b></div>
<nav class="abs nav"><a class="active">Home</a><a>About Us</a><a>Support</a><a>Clients</a><a>Careers</a><a>Contact</a></nav>

<!-- hero -->
<div class="abs hero" role="img" aria-label="Photo of a hand holding a pen over printed business charts beside a tablet"></div>
<div class="abs hero-shade"></div>
<h1 class="abs hero-title">IT solutions that work for your business</h1>
<div class="abs hero-sub">A full service technology company</div>
<div class="abs btn hero-btn">Read More</div>
<div class="abs arrow" style="left:9px"><svg width="38" height="40" viewBox="0 0 38 40"><path d="M22 13 L15 20 L22 27 Z" fill="#fff"/></svg></div>
<div class="abs arrow" style="left:1153px"><svg width="38" height="40" viewBox="0 0 38 40"><path d="M16 13 L23 20 L16 27 Z" fill="#fff"/></svg></div>
<div class="abs dot" style="left:562px;background:var(--orange)"></div>
<div class="abs dot" style="left:597px;background:#fff"></div>

<!-- IT support solutions -->
<section class="abs support"></section>
<h2 class="abs sec-title" style="top:746px">IT Support Solutions</h2>
<p class="abs sec-lead" style="top:806px">Lorem ipsum dolor sit amet, consectetur adipisicing elit, sed do eiusmod tempor incididunt ut et dolore magna aliqua. Ut enim ad minim veniam</p>

<div class="abs svc-icon" style="left:70px;top:927px"><svg width="44" height="44" viewBox="0 0 44 44"><path d="M8 18 h8 l16 -9 v26 l-16 -9 h-8 z" fill="#f47b20"/><rect x="12" y="26" width="5" height="9" fill="#f47b20"/></svg></div>
<div class="abs svc-title" style="left:196px;top:930px">Network Administration</div>
<div class="abs svc-text" style="left:196px;top:957px">Lorem ipsum dolor sit amet, consectetur adipisicing elit</div>

<div class="abs svc-icon" style="left:434px;top:927px"><svg width="44" height="44" viewBox="0 0 44 44"><ellipse cx="22" cy="20" rx="16" ry="12" fill="#f47b20"/><path d="M12 28 l-3 9 l10 -6 z" fill="#f47b20"/></svg></div>
<div class="abs svc-title" style="left:560px;top:930px">Desktop Support</div>
<div class="abs svc-text" style="left:560px;top:957px">Lorem ipsum dolor sit amet, consectetur adipisicing elit</div>

<div class="abs svc-icon" style="left:801px;top:927px"><svg width="44" height="44" viewBox="0 0 44 44"><path d="M12 32 a8 8 0 0 1 0 -16 a11 11 0 0 1 21 2 a7 7 0 0 1 0 14 z" fill="#f47b20"/><path d="M22 16 v11 m-5 -4 l5 5 l5 -5" stroke="#fff" stroke-width="3" fill="none"/></svg></div>
<div class="abs svc-title" style="left:927px;top:930px">Network Cabling</div>
<div class="abs svc-text" style="left:927px;top:957px">Lorem ipsum dolor sit amet, consectetur adipisicing elit</div>

<div class="abs svc-icon" style="left:70px;top:1069px"><svg width="44" height="44" viewBox="0 0 44 44"><path d="M9 35 C9 15 20 9 36 9 C36 26 28 35 9 35 Z" fill="#f47b20"/><path d="M9 35 L28 17" stroke="#fff" stroke-width="2"/></svg></div>
<div class="abs svc-title" style="left:196px;top:1072px">Wireless Networks</div>
<div class="abs svc-text" style="left:196px;top:1099px">Lorem ipsum dolor sit amet, consectetur adipisicing elit</div>

<div class="abs svc-icon" style="left:434px;top:1069px"><svg width="44" height="44" viewBox="0 0 44 44"><circle cx="17" cy="24" r="9" fill="none" stroke="#f47b20" stroke-width="6" stroke-dasharray="4 3"/><circle cx="31" cy="13" r="6" fill="none" stroke="#f47b20" stroke-width="4" stroke-dasharray="3 2"/><circle cx="32" cy="32" r="5" fill="none" stroke="#f47b20" stroke-width="4" stroke-dasharray="3 2"/></svg></div>
<div class="abs svc-title" style="left:560px;top:1072px">Antivirus Solutions</div>
<div class="abs svc-text" style="left:560px;top:1099px">Lorem ipsum dolor sit amet, consectetur adipisicing elit</div>

<div class="abs svc-icon" style="left:801px;top:1069px"><svg width="44" height="44" viewBox="0 0 44 44"><path d="M22 37 L7 22 A8 8 0 0 1 22 12 A8 8 0 0 1 37 22 Z" fill="#f47b20"/></svg></div>
<div class="abs svc-title" style="left:927px;top:1072px">Network Security</div>
<div class="abs svc-text" style="left:927px;top:1099px">Lorem ipsum dolor sit amet, consectetur adipisicing elit</div>

<!-- flexible solutions -->
<section class="abs flex-bg" role="img" aria-label="Dark blurred office background photo"></section>
<h2 class="abs sec-title flex-title">flexible solutions for your business needs</h2>
<p class="abs flex-lead"><em>Velmarketa</em> is a technology solution provider based in Corvane, Texas. Our goal is to make technology a non-issue for individuals and small to medium size businesses ranging from 5 to 150 Users. Velmarketa has the experience, the tools, high-level technology solutions and training to power your business and your work force. We understand that all business's have one goal in common!</p>

<div class="abs card" style="left:65px;top:1503px">
  <svg width="76" height="76" viewBox="0 0 76 76"><circle cx="38" cy="38" r="28" fill="none" stroke="#3ec6a8" stroke-width="18"/><path d="M38 10 A28 28 0 0 1 66 38" fill="none" stroke="#f5c542" stroke-width="18"/><circle cx="38" cy="38" r="8" fill="#fff"/></svg>
  <h3>Managed IT Solutions</h3>
  <p>Our staff will design, service, administer and maintain your IT needs. We are well versed on all major operating system, and network appliances.</p>
</div>
<div class="abs card" style="left:432px;top:1503px">
  <svg width="76" height="80" viewBox="0 0 76 80"><rect x="32" y="2" width="12" height="8" fill="#e88a1a"/><circle cx="38" cy="44" r="32" fill="#f5a623"/><circle cx="38" cy="44" r="24" fill="#fff"/><path d="M38 44 V26 M38 44 L50 50" stroke="#333" stroke-width="4"/></svg>
  <h3>Remote Diagnostic and Support</h3>
  <p>Do you need a quick solution to a technical problem? With our live remote-assistance tool, a member of our support team can view your desktop and share control of your mouse and keyboard to get you on your way to a solution.</p>
</div>
<div class="abs card" style="left:798px;top:1503px">
  <svg width="80" height="80" viewBox="0 0 80 80"><path d="M8 20 L22 8 L48 34 L36 46 Z" fill="#c8c2b4"/><circle cx="50" cy="48" r="22" fill="#c8c2b4"/><circle cx="50" cy="48" r="13" fill="#3d4b52"/><circle cx="50" cy="48" r="6" fill="#5fb87a"/></svg>
  <h3>IT Infrastructure Design and Installation</h3>
  <p style="top:118px">Do you have more than one site? Do you need remote access? We can design and implement LANS/WANS and VPN's. Make your important data available to you wherever you are.</p>
</div>

<div class="abs card short" style="left:65px;top:1870px">
  <svg width="76" height="86" viewBox="0 0 76 86"><circle cx="38" cy="32" r="26" fill="#f5c518"/><rect x="26" y="56" width="24" height="20" rx="3" fill="#9aa0a6"/><path d="M26 63 H50 M26 69 H50" stroke="#6e7378" stroke-width="2"/></svg>
  <h3>SEO Marketing</h3>
  <p>Lorem ipsum dolor sit ame consectetur adipisicing elit</p>
</div>
<div class="abs card short" style="left:432px;top:1870px">
  <svg width="76" height="76" viewBox="0 0 76 76"><rect x="14" y="6" width="46" height="62" rx="5" fill="#2c3e50"/><rect x="19" y="12" width="36" height="48" fill="#3d8fd1"/><circle cx="37" cy="64" r="2" fill="#aaa"/></svg>
  <h3>SEO Marketing</h3>
  <p>Lorem ipsum dolor sit ame consectetur adipisicing elit</p>
</div>
<div class="abs card short" style="left:798px;top:1870px">
  <svg width="80" height="80" viewBox="0 0 80 80"><circle cx="40" cy="40" r="30" fill="none" stroke="#e63b2e" stroke-width="16"/><circle cx="40" cy="40" r="30" fill="none" stroke="#fff" stroke-width="16" stroke-dasharray="18 29.1"/></svg>
  <h3>SEO Marketing</h3>
  <p>Lorem ipsum dolor sit ame consectetur adipisicing elit</p>
</div>

<!-- quick contact / why -->
<section class="abs contact-sec"></section>
<h3 class="abs col-title" style="left:65px;top:2390px">Quick Contact</h3>
<div class="abs rule" style="left:65px;top:2428px;width:521px"></div>
<div class="abs field" style="top:2461px">Name</div>
<div class="abs field" style="top:2512px">E-mail Address</div>
<div class="abs field" style="top:2561px;height:73px">Message</div>
<div class="abs btn send">Send Message</div>

<h3 class="abs col-title" style="left:614px;top:2390px">Why our Clients Like Us</h3>
<div class="abs rule" style="left:614px;top:2428px;width:521px"></div>
<p class="abs why-text">Our clients choose Velmarketa and stay with us because we deliver on every technology need they have. We have a 90% client retention rate. Many of our clients span ten or more years. Whether you need to completely outsource your IT requirements or add advanced insight to your existing IT department, Velmarketa can serve as your complete outsourcing or as a compliment to your IT staff.</p>

<!-- tabs & testimonials -->
<div class="abs tabs-box"></div>
<div class="abs tab-list"></div>
<div class="abs tab" style="top:2818px">Responsive Web Design</div>
<div class="abs tab active" style="top:2865px">Premium Plugin Included</div>
<div class="abs tab" style="top:2912px">Predefine Layout</div>
<div class="abs tab" style="top:2959px">Our Philosopy</div>
<div class="abs tab" style="top:3006px;border-bottom:none">What We Do?</div>
<div class="abs tab-photo" role="img" aria-label="Photo of a smiling group of colleagues"></div>
<div class="abs tab-head">Adipisicing elit</div>
<p class="abs tab-text">There are many variations of passages of Lorem Ipsum available, but the majority have suffered alteration in some form, by injected humour, or randomised words which don't look even slightly believable. If you are going to use.</p>

<div class="abs testi-title">Testimonials</div>
<blockquote class="abs quote" style="top:2848px">Lorem ipsum dolor sit amet, consectetur adipisicing elit, sed do eiusmod tempor incididunt<cite><b>-John Doe/</b> Director of xyz.com</cite></blockquote>
<blockquote class="abs quote" style="top:2940px">Lorem ipsum dolor sit amet, consectetur adipisicing elit, sed do eiusmod tempor incididunt<cite><b>-John Doe/</b> Director of xyz.com</cite></blockquote>

<!-- footer -->
<footer class="abs footer"></footer>
<h4 class="abs foot-title" style="left:65px">Contact Us</h4>
<div class="abs rule" style="left:65px;top:3246px;width:245px"></div>
<div class="abs foot-text" style="left:65px;top:3256px">Phone: 12345678<br>Email: xxxxx@mailbox.com<br>Fax: xxxxxxxxxxx</div>

<h4 class="abs foot-title" style="left:341px">Address</h4>
<div class="abs rule" style="left:341px;top:3246px;width:245px"></div>
<div class="abs foot-text" style="left:341px;top:3256px;width:240px;line-height:20px;padding-top:4px">abcd/2 abc Road, city, state, country, 11212121</div>

<h4 class="abs foot-title" style="left:614px">Newsletter</h4>
<div class="abs rule" style="left:614px;top:3246px;width:245px"></div>
<div class="abs news-field">E-mail Address</div>
<div class="abs btn join">Join</div>

<h4 class="abs foot-title" style="left:887px">Social Links</h4>
<div class="abs rule" style="left:887px;top:3246px;width:248px"></div>
<div class="abs social-foot" aria-label="Social links"><span></span><span></span><span></span><span></span><span></span></div>

<div class="abs orange-line"></div>
<div class="abs bottombar"></div>
<div class="abs copy">Copyright © 2007 - Velmarketa Group, Inc - All rights reserved</div>
<div class="abs foot-nav"><span>Home</span><span>About Us</span><span>Testimonial</span><span>Contact Us</span></div>

</body>
</html>
```